Business Cards for IT Consulting Company (Managed Service Provider)

I am looking to have some business cards printed and would like some designs. We are an IT Consulting company based in Vancouver BC. I would like a nice clean and modern look to the cards. I have uploaded all the versions of my logo so parts can be used as needed. Here is a snippit from our website homepage:

Kelbrook Systems Ltd. is an IT Solutions Partner located in Vancouver BC, Canada. We offer IT solutions and support to customers in the greater Vancouver Area. With expertise in Microsoft platforms, as well as Linux and Mac OSX and over 12 years experience in the IT industry, Kelbrook Systems is dedicated to offering our clients top quality service and products. We take pride in the solutions we offer our customers. The greatest compliment a client can give us is to recommend our services.

Kelbrook Systems Ltd. offers a wide range of IT services from onsite service to remote support and managed service solutions. This allows clients to choose the support path that best suits their company’s needs. Supporting many different sized companies from small to enterprise level over the past 12 years Kelbrook Systems has the experience and expertise needed to ensure things run smoothly. Allowing our clients to focus on doing business.

Revolutionizing the way IT services are delivered.

Kelbrook Systems is dedicated to providing our clients with IT solutions that work and grow with them for years to come. This philosophy helps save money in the long run instead of replacing equipment constantly. Far too often IT solutions are not well thought out and while possibly solving the problem at hand, require replacement due to growth or quality within a very short time frame. Kelbrook Systems takes pride in providing solutions that will last and be able to accommodate growth without the need for replacement.

Industry/Entity Type

Information Technology

Contact Information for Business Card

Kelbrook Systems Ltd.
(Employee Name)
Eml: (Employees Email Address)
Web: kelbrook.me
Ph: 604-555-0142

Font styles to use
Serif
Sans Serif

Requirements
Must have
• The Company logo and company colors.
Nice to have
• - Our tag line: "Revolutionizing IT Services" or "Revolutionizing the way IT services are delivered."
• - Also I really like the idea of nature and technology together blending which is sort of where my logo came from so integrating that somehow onto the business cards would be great.

```html
<!DOCTYPE html>
<html lang="en">
<head>
<meta charset="utf-8">
<title>Kelbrook Systems Ltd. – Business Card</title>
<link rel="stylesheet" href="https://fonts.googleapis.com/css2?family=Open+Sans:wght@400;600;700&display=swap">
<style>
  :root {
    --backdrop: #2b2c30;
    --card-front: #ffffff;
    --card-back: #58595b;
    --brand-blue: #1ba3e6;
    --text-light: #ffffff;
    --card-w: 540px;
    --card-h: 309px;
  }
  * { box-sizing: border-box; margin: 0; padding: 0; }
  html, body {
    width: 1200px;
    height: 864px;
    overflow: hidden;
    background: var(--backdrop);
    font-family: "Open Sans", Arial, sans-serif;
  }
  .card {
    position: absolute;
    width: var(--card-w);
    height: var(--card-h);
    border-radius: 3px;
  }
  .card--front {
    left: 330px;
    top: 80px;
    background: var(--card-front);
    display: flex;
    align-items: center;
    justify-content: center;
  }
  .brand {
    display: flex;
    align-items: center;
    gap: 14px;
    color: var(--brand-blue);
    font-weight: 600;
    font-size: 30px;
    letter-spacing: 0.2px;
  }
  .brand__square {
    width: 30px;
    height: 30px;
    background: var(--brand-blue);
  }
  .card--back {
    left: 330px;
    top: 470px;
    background: var(--card-back);
    color: var(--text-light);
    text-align: center;
    padding-top: 58px;
  }
  .person-name {
    font-weight: 700;
    font-size: 19px;
    margin-bottom: 20px;
  }
  .contact-list {
    list-style: none;
    font-size: 14px;
    line-height: 21px;
  }
  .contact-list__label { font-weight: 700; }
  .tagline {
    margin-top: 20px;
    font-weight: 600;
    font-size: 16px;
    letter-spacing: 0.3px;
    text-transform: uppercase;
  }
</style>
</head>
<body>
  <section class="card card--front" aria-label="Card front">
    <div class="brand">
      <span class="brand__square" aria-hidden="true"></span>
      <span class="brand__name">Kelbrook Systems Ltd.</span>
    </div>
  </section>

  <section class="card card--back" aria-label="Card back">
    <p class="person-name">Daniel Hart</p>
    <ul class="contact-list">
      <li><span class="contact-list__label">T:</span> 604-555-0142</li>
      <li><span class="contact-list__label">E:</span> info@kelbrook.me</li>
      <li><span class="contact-list__label">W:</span> www.kelbrook.me</li>
    </ul>
    <p class="tagline">Revolutionizing IT Services</p>
  </section>
</body>
</html>
```